" É uma pequena fábrica com injetoras plásticas, e a produção poderá ser a mais variada possível. Podemos, por exemplo, criar desde utensílios plásticos (cabide, potes, baldes), brinquedos e, até mesmo, peças para indústrias. Temos também a parte de reciclagem, onde tratamos o plástico desde o lixo até a produção destes itens. No meu ponto de vista deve ser algo genérico, que demonstre criação, inovação, transformação, visão de futuro. "

```html
<!DOCTYPE html>
<html lang="pt-BR">
<head>
<meta charset="utf-8">
<title>Moldara – Cartão de visita</title>
<link rel="stylesheet" href="https://fonts.googleapis.com/css2?family=Montserrat:wght@400;500;600;700;800&display=swap">
<style>
  :root {
    --navy: #1b2d52;
    --navy-deep: #142343;
    --orange: #f07d1a;
    --white: #ffffff;
    --ink: #3b3f47;
    --muted: #6d717a;
    --facet: #eceef1;
    --facet-dark: #e1e4e8;
    --backdrop: #d9dadc;
  }
  * { box-sizing: border-box; margin: 0; padding: 0; }
  html, body { width: 1200px; height: 1200px; overflow: hidden; }
  body {
    background: var(--backdrop);
    font-family: "Montserrat", sans-serif;
    display: flex;
    flex-direction: column;
    align-items: center;
    justify-content: center;
    gap: 70px;
  }
  .card {
    width: 900px;
    height: 514px;
    border-radius: 30px;
    position: relative;
    overflow: hidden;
  }
  /* Front: contact side */
  .card-front { background: var(--white); }
  .card-front .facets { position: absolute; inset: 0; }
  .identity {
    position: absolute;
    left: 70px;
    top: 70px;
    padding-left: 22px;
    border-left: 5px solid var(--orange);
  }
  .identity .name {
    color: var(--orange);
    font-weight: 700;
    font-size: 34px;
    letter-spacing: 0.5px;
    line-height: 1.1;
  }
  .identity .role {
    color: var(--muted);
    font-weight: 500;
    font-size: 26px;
    margin-top: 4px;
  }
  .contacts {
    position: absolute;
    left: 70px;
    top: 210px;
    list-style: none;
    display: flex;
    flex-direction: column;
    gap: 18px;
  }
  .contacts li {
    display: flex;
    align-items: flex-start;
    gap: 16px;
    color: var(--ink);
    font-size: 20px;
    font-weight: 500;
    line-height: 1.25;
  }
  .contacts .icon {
    width: 30px;
    height: 30px;
    flex: none;
    border-radius: 50%;
    background: var(--orange);
    display: flex;
    align-items: center;
    justify-content: center;
  }
  .contacts .icon svg { width: 16px; height: 16px; }
  .front-name {
    position: absolute;
    right: 80px;
    top: 230px;
    color: var(--navy);
    font-weight: 800;
    font-size: 54px;
    letter-spacing: 2px;
  }
  /* Back: brand side */
  .card-back {
    background: linear-gradient(160deg, var(--navy) 0%, var(--navy-deep) 100%);
    display: flex;
    flex-direction: column;
    align-items: center;
    justify-content: center;
    gap: 14px;
  }
  .brand-row { display: flex; align-items: center; gap: 22px; }
  .brand-dot {
    width: 34px; height: 34px; border-radius: 50%;
    background: var(--orange);
  }
  .brand-name {
    color: var(--white);
    font-weight: 800;
    font-size: 104px;
    letter-spacing: 4px;
    line-height: 1;
  }
  .brand-tagline {
    color: var(--white);
    font-weight: 500;
    font-size: 28px;
    letter-spacing: 10px;
  }
</style>
</head>
<body>
  <section class="card card-front">
    <svg class="facets" viewBox="0 0 900 514" preserveAspectRatio="none" aria-hidden="true">
      <polygon points="430,514 900,120 900,514" fill="var(--facet)"/>
      <polygon points="620,514 900,280 900,514" fill="var(--facet-dark)"/>
      <rect x="0" y="506" width="900" height="8" fill="var(--orange)"/>
    </svg>

    <div class="identity">
      <p class="name">NOME E SOBRENOME</p>
      <p class="role">Cargo | Função</p>
    </div>

    <ul class="contacts">
      <li>
        <span class="icon"><svg viewBox="0 0 24 24" fill="#fff"><path d="M6.6 10.8a15.1 15.1 0 0 0 6.6 6.6l2.2-2.2a1 1 0 0 1 1-.25 11.4 11.4 0 0 0 3.6.57 1 1 0 0 1 1 1V20a1 1 0 0 1-1 1A17 17 0 0 1 3 4a1 1 0 0 1 1-1h3.5a1 1 0 0 1 1 1c0 1.25.2 2.45.57 3.57a1 1 0 0 1-.25 1z"/></svg></span>
        (00) 0000-0000
      </li>
      <li>
        <span class="icon"><svg viewBox="0 0 24 24" fill="#fff"><path d="M3 5h18v14H3z M3 5l9 7 9-7" stroke="#f07d1a" stroke-width="1.6"/></svg></span>
        contato@exemplo.com
      </li>
      <li>
        <span class="icon"><svg viewBox="0 0 24 24" fill="none" stroke="#fff" stroke-width="2"><circle cx="12" cy="12" r="9"/><path d="M3 12h18M12 3c3 3 3 15 0 18M12 3c-3 3-3 15 0 18"/></svg></span>
        www.exemplo.com
      </li>
      <li>
        <span class="icon"><svg viewBox="0 0 24 24" fill="#fff"><path d="M12 2a7 7 0 0 0-7 7c0 5 7 13 7 13s7-8 7-13a7 7 0 0 0-7-7zm0 9.5A2.5 2.5 0 1 1 12 6.5a2.5 2.5 0 0 1 0 5z"/></svg></span>
        <span>rua exemplo, sl 000<br>cidade-UF, CEP: 00000-000</span>
      </li>
    </ul>

    <p class="front-name">MOLDARA</p>
  </section>

  <section class="card card-back">
    <div class="brand-row">
      <span class="brand-dot"></span>
      <p class="brand-name">MOLDARA</p>
    </div>
    <p class="brand-tagline">INJEÇÃO PLÁSTICA</p>
  </section>
</body>
</html>
```